■依頼の目的
2月に出版予定の電子書籍

タイトル:後悔しない住まい手配ガイド決定版2021
サブタイトル:[特集]三世代でつなぐ暮らし設計
著者:一級建築士 柚木湊

キャッチコピー:コロナ対応住宅チェックリスト付き!

※追加テキスト
家づくりの補助金
4月に省エネ説明義務化
IoT住宅の現在

キャッチコピー等の配置はPDFに記載

の表紙デザインをお願いします。

■本の内容
・年一回発行する雑誌形式の電子書籍
・住宅会社選びの方法を紹介
・特集記事や時事ネタも扱う

■デザイン要望
・30代~40代の子育て夫婦に好まれるデザインを希望
・LivoMarqueのようなお洒落な家づくり雑誌の雰囲気
・過去の4作品との差別化(過去表紙はPDFに)
・最新作であることがわかるよう「2021」を目立つように

■キャッチ等の変更の可能性あり
お願いする方が決まった後、キャッチコピーなどの文字を若干変更する可能性があります。

■添付ファイルについて
・必要な配置をPDFに添付しています
・ロゴのaiデータ添付します

その他何かご不明な点がございましたら、お気軽にご質問下さい。
よろしくお願いいたします。
・Pebble magazine というタイトルの色は、変えるようにしてください。
年一回の雑誌なので、毎年、ちがう色を使っています。
過去の作品と被らないように色提案をお願いします。
・文字はスマホで見た時にも、読めることを意識してください。
・背景の写真・イラストのセレクトが重要になります。livoなどのインテリア雑誌などを参考にしてください。

写真の選び方が秀逸でした。
シンメトリーを意識したモダンな建物外観が素晴らしく、それを引き立たせるようなデザインで、見た瞬間、これしかないと思わせるものでした。
今回は、私のメルマガ読者200人にアンケートを行って半数の方がこのデザインを支持しました。

この度は、沢山のご提案を頂きありがとうございました!
毎年、出版しているシリーズでしたが、雰囲気を一新したいことからコンペを使わせて頂きましたが、様々なデザイン提案を頂き、とても参考になりました。
今後もコンペを使わせて頂きますので、引き続きよろしくお願いいたします!

```html
<!DOCTYPE html>
<html lang="ja">
<head>
<meta charset="utf-8">
<title>Pebble magazine vol.5 2021</title>
<link href="https://fonts.googleapis.com/css2?family=Noto+Sans+JP:wght@500;700;900&family=Cormorant+Garamond:ital,wght@0,500;1,500&display=swap" rel="stylesheet">
<style>
  :root {
    --paper: #ffffff;
    --ink: #111111;
    --logo: #a7b4c6;
    --slate: #8193aa;
    --slate-dark: #6f8199;
    --navy: #1f2a44;
    --feature-red: #c4161c;
    --room-light: #eef1f4;
    --room-mid: #9aa7b6;
    --room-dark: #4a3a30;
  }
  html, body { margin: 0; padding: 0; overflow: hidden; }
  .cover {
    position: relative;
    width: 750px;
    height: 1200px;
    background: var(--paper);
    overflow: hidden;
    font-family: "Noto Sans JP", sans-serif;
    color: var(--ink);
  }
  .masthead {
    position: absolute; left: 25px; top: 14px;
    font-family: "Cormorant Garamond", serif;
    font-weight: 500;
    color: var(--logo);
    line-height: 1;
  }
  .masthead .issue { font-size: 16px; letter-spacing: 1px; display: block; margin-left: 8px; }
  .masthead .name-main { font-size: 112px; display: block; margin-top: 0; }
  .masthead .name-sub { font-size: 54px; display: block; margin-left: 10px; margin-top: -10px; }
  .topics {
    position: absolute; left: 492px; top: 22px;
    margin: 0; padding: 0; list-style: none;
    font-weight: 900; font-size: 22px; line-height: 40px;
    white-space: nowrap;
  }
  .badge {
    position: absolute; left: 606px; top: 146px;
    width: 132px; height: 132px; border-radius: 50%;
    background: var(--navy); color: #fff;
    display: flex; flex-direction: column; align-items: center; justify-content: center;
    font-weight: 900; text-align: center; line-height: 1.15;
  }
  .badge .lead { font-size: 24px; }
  .badge .small { font-size: 16px; }
  .author {
    position: absolute; left: 480px; top: 284px;
    font-weight: 700; font-size: 16px; white-space: nowrap;
  }
  .author strong { font-size: 24px; font-weight: 900; margin-left: 8px; }
  .title-line {
    position: absolute; left: 20px; margin: 0;
    font-weight: 900; line-height: 1; letter-spacing: -2px; white-space: nowrap;
  }
  .title-line.l1 { top: 236px; font-size: 88px; }
  .title-line.l2 { top: 332px; font-size: 80px; }
  .title-line.l3 { top: 468px; font-size: 100px; color: var(--slate); }
  .subtitle-en {
    position: absolute; left: 24px; top: 420px;
    font-family: "Cormorant Garamond", serif; font-style: italic;
    font-size: 36px; line-height: 1; color: #222; white-space: nowrap;
  }
  .photo {
    position: absolute; left: 0; top: 560px; width: 750px; height: 550px;
    background: linear-gradient(180deg, var(--paper) 0%, var(--room-light) 24%, #d5dbe2 46%, var(--room-mid) 68%, #7c7068 86%, var(--room-dark) 100%);
  }
  .year {
    position: absolute; left: 20px; top: 560px;
    font-weight: 900; font-size: 110px; line-height: 1;
    color: var(--slate-dark); letter-spacing: -2px;
  }
  .feature {
    position: absolute; left: 0; top: 1110px; width: 750px; height: 90px;
    background: var(--paper);
    display: flex; align-items: center; gap: 16px; padding-left: 28px; box-sizing: border-box;
  }
  .feature .tag {
    background: var(--feature-red); color: #fff;
    width: 50px; height: 56px; display: flex; align-items: center; justify-content: center;
    font-weight: 900; font-size: 20px; line-height: 1; writing-mode: vertical-rl;
  }
  .feature .text { font-weight: 900; font-size: 50px; letter-spacing: -1px; white-space: nowrap; }
</style>
</head>
<body>
<div class="cover">
  <div class="masthead">
    <span class="issue">vol.5 2021</span>
    <span class="name-main">Pebble</span>
    <span class="name-sub">magazine</span>
  </div>

  <ul class="topics">
    <li>家づくりの補助金</li>
    <li>4月に省エネ説明義務化</li>
    <li>IoT 住宅の現在</li>
  </ul>

  <div class="badge">
    <span class="lead">コロナ</span>
    <span class="lead">対応住宅</span>
    <span class="small">チェックリスト</span>
    <span class="small">付き!</span>
  </div>

  <div class="author">一級建築士<strong>柚木湊</strong></div>

  <div class="photo" role="img" aria-label="明るい窓辺に二つの洗面台が並ぶモダンな洗面室のインテリア写真"></div>

  <h1 class="title">
    <span class="title-line l1">後悔しない</span>
    <span class="title-line l2">住まい手配ガイド</span>
    <span class="title-line l3">決定版</span>
  </h1>
  <div class="subtitle-en">How to choose the best house maker &amp; contractor</div>
  <div class="year">2021</div>

  <div class="feature">
    <span class="tag">特集</span>
    <span class="text">三世代でつなぐ暮らし設計</span>
  </div>
</div>
</body>
</html>
```